Skincare company needing leaflet/flyer for selling products

Hi guys. I am needing a leaflet/flyer design for my new skincare business - Tovani skincare. Our products are all made in Australia from natural ingredients. The leaflet should specify that all products have - organic ingredients, cruelty free, no nasty chemicals or ingredients and a made in Australia logo.
The pictures I have supplied, if they can be made more professional looking for the design without any background that would be great. It should look like other competitors and very appealing. The leaflet can be double sided so it looks more easy to read
The information is provided as follows:
Product, skin types the product is for, ml capacity of bottle, key ingredients and price.
Contact is a whatsapp number and website will be up later so if a leaflet can be made with and without the website.
This leaflet/flyer can be easy to read, not hard on the eyes and easy to understand. Focus on blue shades and other calm colours to make it easy on the eyes and attractive to see. Thank you guys for helping
Getting professional product photos done that can be updated on the leaflet/flyers once received. More submissions are welcomed
People wanting good quality skincare that does not contain harmful chemicals and is organic

```html
<!DOCTYPE html>
<html lang="en">
<head>
<meta charset="utf-8">
<title>Tovani Skincare – Product Leaflet</title>
<link href="https://fonts.googleapis.com/css2?family=Questrial&family=Mulish:wght@800&display=swap" rel="stylesheet">
<style>
:root{
  --backdrop:#bdbec2;
  --page-top:#e6e9ef;
  --page:#f3f6fa;
  --ink:#111318;
  --navy:#121a33;
  --sky:#7e9fcc;
  --divider:#9bb0c8;
  --pipe:#e3a9a9;
  --pill-line:#33a9d6;
  --wave:#c9d4e6;
  --price-black:#050505;
  --price-cyan:#1ea9d9;
  --price-tan:#c8ad95;
  --price-blue:#7fa5d0;
  --price-gold:#c8bf3a;
}
*{margin:0;padding:0;box-sizing:border-box}
html,body{width:1200px;height:1200px;overflow:hidden}
body{background:var(--backdrop);position:relative;font-family:"Questrial",sans-serif;color:var(--ink)}
.page{position:absolute;top:109px;width:462px;height:981px;overflow:hidden;
  background:linear-gradient(180deg,var(--page-top) 0%,var(--page) 35%,#f7f9fc 100%);
  box-shadow:0 2px 8px rgba(0,0,0,.12)}
.page--front{left:131px}
.page--back{left:607px;height:982px}
.wave{position:absolute;left:0;bottom:0;width:100%;height:90px}
.hero-photo{position:absolute;right:0;top:19px;width:196px;height:266px;
  background:radial-gradient(ellipse at 55% 40%,#e9c2a6 0%,#d9a9a3 35%,#e3cdd2 65%,rgba(230,233,239,0) 100%);
  border-bottom-left-radius:60% 40%}
.hero-curve{position:absolute;left:0;top:215px;width:100%;height:90px}
.brand{position:absolute;left:50px;top:46px;width:200px;text-align:center;color:var(--navy)}
.brand-mark{width:68px;height:68px;background:var(--navy);margin:0 auto 14px}
.brand-name{font-size:34px;letter-spacing:8px;line-height:1;padding-left:8px}
.brand-sub{font-size:11px;letter-spacing:6px;margin-top:6px;padding-left:6px}
.claims{position:absolute;top:219px;left:37px;display:flex;gap:7px;z-index:2}
.claim{width:52px;height:52px;border-radius:50%;border:2px solid var(--ink);display:flex;align-items:center;justify-content:center;background:#fff;box-shadow:inset 0 0 0 5px #fff,inset 0 0 0 6.5px var(--ink)}
.claim::after{content:"";width:22px;height:22px;border-radius:50%;background:var(--ink)}
.product{position:absolute;left:0;width:100%;height:200px}
.product-photo{position:absolute;left:52px;top:12px;width:40px;height:132px;border-radius:6px 6px 10px 10px;
  background:linear-gradient(90deg,#d6dbe2,#fbfcfd 40%,#e8ecf1 80%,#c9ced6)}
.product-photo--dropper{background:linear-gradient(90deg,#1a1a1a,#3b3b3b 45%,#111);border-radius:14px 14px 12px 12px;width:44px;left:50px;top:22px;height:120px}
.product-photo--jar{left:28px;top:60px;width:80px;height:56px;border-radius:10px}
.product-photo--short{top:40px;height:110px}
.volume{position:absolute;left:37px;top:160px;width:66px;height:24px;border:1.5px solid var(--pill-line);border-radius:12px;background:#fff;
  font-size:12px;display:flex;align-items:center;justify-content:center}
.info{position:absolute;left:132px;top:0;width:305px}
.info h2{font-weight:400;font-size:15.5px;letter-spacing:.2px;line-height:1.2}
.skin-types{font-size:11.5px;color:var(--sky);margin-top:5px}
.skin-types .pipe{color:var(--pipe);margin:0 4px}
.price{position:absolute;right:0;top:-4px;width:42px;height:42px;border-radius:50%;color:#fff;
  font-size:13px;display:flex;align-items:center;justify-content:center}
.key-label{display:flex;align-items:center;margin:11px 0 6px;font-family:"Mulish",sans-serif;font-size:6.8px;letter-spacing:.8px}
.key-label::before{content:"";flex:1;height:1px;background:var(--divider);margin-right:6px}
.key-label::after{content:"";width:28px;height:1px;background:var(--divider);margin-left:6px}
.ingredient{margin-bottom:4px}
.ingredient h3{font-family:"Mulish",sans-serif;font-weight:800;font-size:10.3px;line-height:1.2}
.ingredient p{font-size:9.9px;line-height:1.22}
.rule{position:absolute;left:132px;width:305px;top:181px;height:1px;background:var(--divider)}
.contact{position:absolute;display:flex;align-items:center;gap:8px;font-size:24px;letter-spacing:.5px}
.contact--box{left:138px;top:933px;width:186px;height:40px;background:var(--navy);color:#fff;justify-content:center;font-size:19px}
.contact--plain{left:262px;top:928px;font-family:"Mulish",sans-serif;font-weight:800;color:var(--ink)}
.contact svg{flex:none}
</style>
</head>
<body>

<section class="page page--front">
  <div class="hero-photo" role="img" aria-label="Smiling woman in a pink headscarf resting her chin on her hand"></div>
  <svg class="hero-curve" viewBox="0 0 462 90" preserveAspectRatio="none"><path d="M0 40 Q60 10 180 30 Q300 55 462 40 L462 90 L0 90Z" fill="#eef2f8"/></svg>

  <div class="brand">
    <div class="brand-mark"></div>
    <div class="brand-name">TOVANI</div>
    <div class="brand-sub">SKINCARE</div>
  </div>

  <div class="claims">
    <span class="claim" role="img" aria-label="Organic ingredients badge"></span>
    <span class="claim" role="img" aria-label="Cruelty free badge"></span>
    <span class="claim" role="img" aria-label="No nasty chemicals badge"></span>
    <span class="claim" role="img" aria-label="Made in Australia badge"></span>
  </div>

  <article class="product" style="top:301px">
    <div class="product-photo" role="img" aria-label="Hydrating moisturiser pump bottle"></div>
    <div class="volume">60ML</div>
    <div class="info">
      <h2>HYDRATING MOISTURISER</h2>
      <div class="skin-types">Normal<span class="pipe">|</span>Dry<span class="pipe">|</span>Mature Skin Types</div>
      <div class="price" style="background:var(--price-black)">$18</div>
      <div class="key-label">KEY INGREDIENTS</div>
      <div class="ingredient"><h3>ROSEHIP OIL</h3><p>Rich in essential fatty acids which are integral for skin regeneration and boosting collagen formation.</p></div>
      <div class="ingredient"><h3>GREEN TEA LEAF EXTRACT</h3><p>Anti-inflammatory benefits which reduce redness and soothes skin irritation.</p></div>
      <div class="ingredient"><h3>DAVIDSON PLUM EXTRACT</h3><p>Improves the appearance of fine lines and wrinkles and rich in antioxidants.</p></div>
    </div>
    <div class="rule"></div>
  </article>

  <article class="product" style="top:505px">
    <div class="product-photo" role="img" aria-label="Balancing moisturiser pump bottle"></div>
    <div class="volume">60ML</div>
    <div class="info">
      <h2>BALANCING MOISTURISER</h2>
      <div class="skin-types">Oily<span class="pipe">|</span>Combination<span class="pipe">|</span>Problematic Skin Types</div>
      <div class="price" style="background:var(--price-cyan)">$18</div>
      <div class="key-label">KEY INGREDIENTS</div>
      <div class="ingredient"><h3>GRAPE SEED OIL</h3><p>Acts as an anti-inflammatory and effective in combating acne.</p></div>
      <div class="ingredient"><h3>LICORICE ROOT EXTRACT</h3><p>Provides skin brightening effects and soothes itchy and irritated skin.</p></div>
      <div class="ingredient"><h3>QUANDONG (SANDALWOOD) EXTRACT</h3><p>High in vitamin C, reduces the appearance of ageing such as dark circles and pigmentation.</p></div>
    </div>
    <div class="rule"></div>
  </article>

  <article class="product" style="top:710px">
    <div class="product-photo product-photo--short" role="img" aria-label="Eye cream pump bottle"></div>
    <div class="volume">15ML</div>
    <div class="info">
      <h2>EYE CREAM</h2>
      <div class="skin-types">All Skin Types</div>
      <div class="price" style="background:var(--price-tan)">$19</div>
      <div class="key-label">KEY INGREDIENTS</div>
      <div class="ingredient"><h3>CUCUMIS SATIVUS (CUCUMBER) SEED OIL</h3><p>Highly moisturising with Vitamin E, it balances the skin &amp; encourages healthy skin regeneration.</p></div>
      <div class="ingredient"><h3>KAKADU PLUM EXTRACT</h3><p>Rich in Vitamin C &amp; Gallic acid which has anti-inflammatory properties, can help reduce pigmentation and dark spots.</p></div>
      <div class="ingredient"><h3>QUANDONG EXTRACT</h3><p>High in Rutin, an antioxidant that soothes skin and calms redness, it also reduces the signs of ageing.</p></div>
    </div>
    <div class="rule" style="top:197px"></div>
  </article>

  <svg class="wave" viewBox="0 0 462 90" preserveAspectRatio="none"><path d="M0 35 Q120 0 260 30 Q380 55 462 20 L462 90 L0 90Z" fill="var(--wave)"/></svg>
  <div class="contact contact--box">
    <svg width="22" height="22" viewBox="0 0 24 24"><path d="M6.6 10.8c1.4 2.8 3.8 5.1 6.6 6.6l2.2-2.2c.3-.3.7-.4 1-.2 1.1.4 2.3.6 3.6.6.6 0 1 .4 1 1V20c0 .6-.4 1-1 1C10.6 21 3 13.4 3 4c0-.6.4-1 1-1h3.5c.6 0 1 .4 1 1 0 1.3.2 2.5.6 3.6.1.3 0 .7-.2 1z" fill="#fff"/></svg>
    0487210553
  </div>
</section>

<section class="page page--back">
  <article class="product" style="top:29px">
    <div class="product-photo" style="top:0;height:168px" role="img" aria-label="Facial cleansing gel pump bottle"></div>
    <div class="volume" style="top:198px">125ML</div>
    <div class="info">
      <h2>FACIAL CLEANSING GEL</h2>
      <div class="skin-types">Oily<span class="pipe">|</span>Combination<span class="pipe">|</span>Problematic Skin Types</div>
      <div class="price" style="background:var(--price-blue)">$20</div>
      <div class="key-label">KEY INGREDIENTS</div>
      <div class="ingredient"><h3>VITAMIN E</h3><p>A natural antioxidant that helps to protect the face from exposure to the sun and increases skin elasticity. It also reduces acne, blemishes and soothes the skin.</p></div>
      <div class="ingredient"><h3>ALOE VERA JUICE</h3><p>Hydrates &amp; exfoliates the face, reducing inflammation, acne and dry skin.</p></div>
      <div class="ingredient"><h3>KAKADU PLUM EXTRACT</h3><p>Rich in Vitamin C &amp; Gallic acid which has anti-inflammatory properties, can help reduce pigmentation and dark spots. Also stimulates growth of collagen.</p></div>
    </div>
    <div class="rule" style="top:211px"></div>
  </article>

  <article class="product" style="top:256px">
    <div class="product-photo product-photo--dropper" role="img" aria-label="Vitamin C serum dropper bottle"></div>
    <div class="volume" style="top:176px">30ML</div>
    <div class="info">
      <h2>VITAMIN C SERUM</h2>
      <div class="skin-types">All Skin types</div>
      <div class="price" style="background:var(--price-tan)">$15</div>
      <div class="key-label">KEY INGREDIENTS</div>
      <div class="ingredient"><h3>SODIUM PHYTATE</h3><p>Contains stabilising properties that moisturises the skin, helps reduce pore size and improve the appearance of cellulite</p></div>
      <div class="ingredient"><h3>DAVIDSON PLUM EXTRACT</h3><p>Improves the appearance of fine lines and wrinkles and rich in antioxidants.</p></div>
      <div class="ingredient"><h3>VITAMIN C (SODIUM ASCORBYL PHOSPHATE)</h3><p>Contains anti-inflammatory and anti-ageing properties and helps fight acne and blemishes.</p></div>
    </div>
    <div class="rule" style="top:199px"></div>
  </article>

  <article class="product" style="top:464px">
    <div class="product-photo" style="top:0;height:168px" role="img" aria-label="Perfecting toning mist spray bottle"></div>
    <div class="volume" style="top:188px">125ML</div>
    <div class="info">
      <h2>PERFECTING TONING MIST</h2>
      <div class="skin-types">All Skin types</div>
      <div class="price" style="background:var(--price-black)">$17.5</div>
      <div class="key-label">KEY INGREDIENTS</div>
      <div class="ingredient"><h3>ROSE FLOWER WATER</h3><p>Contains anti-ageing properties, hydrates the skin and soothes skin irritation.</p></div>
      <div class="ingredient"><h3>GREEN TEA LEAF EXTRACT</h3><p>Anti-inflammatory benefits which reduce redness and soothes skin irritation.</p></div>
      <div class="ingredient"><h3>KAKADU PLUM</h3><p>Rich in Vitamin C &amp; Gallic acid which has anti-inflammatory properties, can reduce pigmentation and dark spots. It also stimulates growth of collagen and reduces wrinkles.</p></div>
    </div>
    <div class="rule" style="top:211px"></div>
  </article>

  <article class="product" style="top:686px">
    <div class="product-photo product-photo--jar" role="img" aria-label="Body balm jar with yellow label"></div>
    <div class="volume" style="top:186px">250ML</div>
    <div class="info">
      <h2>BODY BALM</h2>
      <div class="skin-types">Oily<span class="pipe">|</span>Combination<span class="pipe">|</span>Problematic Skin Types</div>
      <div class="price" style="background:var(--price-gold)">$15</div>
      <div class="key-label">KEY INGREDIENTS</div>
      <div class="ingredient"><h3>KAKADU PLUM EXTRACT</h3><p>Rich in Vitamin C &amp; Gallic acid which has anti-inflammatory properties, can help reduce pigmentation and dark spots. Also stimulates growth of collagen.</p></div>
      <div class="ingredient"><h3>PANTHENOL (VITAMIN B5)</h3><p>An anti-inflammatory skin barrier repairer that improves the appearance of skin, preventing dryness and keeping the skin balanced</p></div>
      <div class="ingredient"><h3>DESERT LIME EXTRACT</h3><p>High in Vitamin C &amp; antioxidants, it vitalises the skin, keeping it nourished and rejuvenated.</p></div>
    </div>
    <div class="rule" style="top:218px"></div>
  </article>

  <svg class="wave" viewBox="0 0 462 90" preserveAspectRatio="none"><path d="M0 20 Q140 0 280 40 Q390 70 462 30 L462 90 L0 90Z" fill="#dfe5ef"/></svg>
  <div class="contact contact--plain">
    <svg width="28" height="28" viewBox="0 0 24 24"><path d="M6.6 10.8c1.4 2.8 3.8 5.1 6.6 6.6l2.2-2.2c.3-.3.7-.4 1-.2 1.1.4 2.3.6 3.6.6.6 0 1 .4 1 1V20c0 .6-.4 1-1 1C10.6 21 3 13.4 3 4c0-.6.4-1 1-1h3.5c.6 0 1 .4 1 1 0 1.3.2 2.5.6 3.6.1.3 0 .7-.2 1z" fill="var(--ink)"/></svg>
    0487210553
  </div>
</section>

</body>
</html>
```